Tovren Bay Healthcare of Lauderhill

A website design for this primary care physician practice, featuring latino, caucasian and black patients and employees.

Target Market(s)

LATIN, INDIAN, ASIAN, CARIBBEAN/BLACK, AND CAUCASIAN PATIENTS.

Coding

Coded - Design and coding required

Number of Pages Required

4 page

Requirements
Must have
• 1. MULTICULTURAL PICTURES OF PATIENTS AND EMPLOYEES
• 2. About Us
• We specialize in internal medicine and offer a full range of primary care and family medical services. We are dedicated to your well-being and ensure continuity of care every time you visit our office. Our staff works with patients to understand their lifestyle and needs to continually deliver the best care possible. If you are looking for a primary healthcare provider and a quality experience, feel free to contact us to schedule an appointment today.
• Family Health Care
• Our clinical team is ready to serve the entire family and provide the most advanced and personalized care available today.
• 3. Schedule An Appointment
• We are open Monday through Friday from 9am to 4:30pm.
• Same Day Availability
• 4. Our focus is to provide our patients with life-long care and to be readily available for immediate and unexpected emergencies.
• Flu, Headaches and Pain
• Everyday illnesses, aches and pains can set you back at work and at home. Our commitment is to get you back to your daily activities quickly.
• 5. Chronic Disease Management
• Many people suffer from numerous types of chronic diseases every day, and when it comes to chronic disease management, early detection and treatment are crucial to living a healthy life. Helping Patients Live the Most Active Life Possible. So here at Tovren-Bay Health Care, we take pride in serving patients who suffer from chronic diseases and help them live the most active life possible.
• If you are already diagnosed or think you may have a potential issue, come see us to receive help and start managing your chronic disease. We take pride in delivering personalized care for life. We see you through more than just doctor’s appointment, we take care of you through it all.
• Chronic Diseases We Treat
• Fibromyalgia Congestive Heart Failure
• High Blood Pressure Congestive Obstructive Pulmonary Disease
• High Cholesterol
• Diabetes
• 6. Our Founder, Dr. Marcus Penwright
• Why I Became an Internal Medicine Doctor
• I chose Primary Care Internal Medicine because I wanted to get to know patients over time, to see a broad array of different kinds of illnesses, treat the whole patient (not just one body part), learn and help with the physical and mental health of my patients and most importantly, form relationships with them.
• I would love to meet you and would be honored if you choose me as your primary care physician. I chose Internal Medicine for my residency because in Internal Medicine the focus is on adults and more complex patients.
• I have enjoyed the more than 25 years I have spent as an internal medicine doctor and I am very happy with the patient relationships I have established in the course of my practice. I would love to meet you and would be honored if you choose me as your primary care physician.
• Marcus Penwright, MD
• 7. Locations
• Tovren-Bay Healthcare Center
• 2716 Orchid Fern Rd
• Greenacres, Florida 33471
• Office: (561) 555-0182
• Fax: (561) 555-0147
• 5130 N. Harborview Ave, Suite 304
• Lauderhill, Florida 33328
• Office: (954) 555-0136
• Fax: (954) 555-0173
• * Both locations are open Monday through Friday from 9am to 4:30pm.
Nice to have
• BRIGHT FLORIDA/CARIBBEAN COLORS

```html
<!DOCTYPE html>
<html lang="en">
<head>
<meta charset="utf-8">
<title>Tovren Bay Healthcare</title>
<link rel="stylesheet" href="https://fonts.googleapis.com/css2?family=Montserrat:wght@400;500;600;700&family=Raleway:wght@500;600;700&family=PT+Sans:wght@400;700&display=swap">
<style>
:root{
  --blue:#1a75c2;
  --green:#5ab243;
  --ink:#222326;
  --text:#555;
  --light:#efeff1;
  --footer:#3b3c3f;
  --footer-line:#55575b;
  --white:#fff;
  --star:#e8542f;
}
*{margin:0;padding:0;box-sizing:border-box}
html,body{width:1200px;height:2995px;overflow:hidden}
body{font-family:"PT Sans",Arial,sans-serif;color:var(--text);background:var(--white);position:relative}
.abs{position:absolute}
.section-title{position:absolute;left:0;width:1200px;text-align:center;font-family:"Montserrat",Arial,sans-serif;font-weight:600;font-size:19px;color:var(--ink);letter-spacing:.5px}
.section-title::after{content:"";display:block;width:76px;height:2px;background:#bbb;margin:10px auto 0}
.btn{position:absolute;display:flex;align-items:center;justify-content:center;font-family:"Montserrat",Arial,sans-serif;font-weight:600;font-size:11px;letter-spacing:.5px;text-transform:uppercase}

/* hero */
.hero{position:absolute;left:0;top:0;width:1200px;height:655px;background:linear-gradient(180deg,#4c5a86 0%,#7a6f9a 22%,#b7849a 38%,#6f7f9c 55%,#3c4a55 70%,#6a5a60 82%,#2d3438 100%)}
.brand{position:absolute;left:130px;top:20px;font-family:"Raleway",Arial,sans-serif;font-weight:700;font-size:25px;color:var(--white)}
.nav{position:absolute;top:24px;left:556px;display:flex;gap:0}
.nav a{font-family:"Montserrat",Arial,sans-serif;font-size:11px;font-weight:600;color:var(--white);text-decoration:none;padding:7px 10px;margin-right:12px;text-transform:uppercase}
.nav a.active{background:rgba(255,255,255,.85);color:#555}
.hero-kicker{position:absolute;left:0;width:1200px;top:452px;text-align:center;font-family:"Montserrat",Arial,sans-serif;font-size:31px;color:var(--white);font-weight:400}
.hero-title{position:absolute;left:0;width:1200px;top:490px;text-align:center;font-family:"Montserrat",Arial,sans-serif;font-size:34px;color:var(--white);font-weight:700}
.hero .btn{left:534px;top:566px;width:132px;height:40px;border:2px solid var(--white);color:var(--white);font-size:13px}
.slide-arrow{position:absolute;top:282px;width:50px;height:50px;border-radius:50%;background:var(--white);display:flex;align-items:center;justify-content:center}

/* welcome */
.welcome-text{position:absolute;left:400px;width:400px;top:756px;text-align:center;font-size:12px;line-height:20px}
.feature-icon{position:absolute;width:72px;height:72px;border-radius:50%;background:var(--white);border:2px solid #ddd;display:flex;align-items:center;justify-content:center}
.feature-label{position:absolute;font-size:12px;color:#444;text-align:center;width:120px}

/* treatments */
.treatments{position:absolute;left:0;top:1298px;width:1200px;height:552px;background:var(--light)}
.card{position:absolute;top:1438px;width:220px}
.card .photo{width:220px;height:228px}
.card h3{margin-top:26px;text-align:center;font-family:"Montserrat",Arial,sans-serif;font-weight:600;font-size:14px;color:var(--ink)}
.card p{margin:8px auto 0;width:180px;text-align:center;font-size:11px;line-height:17px}
.card .btn{position:relative;margin:16px auto 0;width:98px;height:26px;background:var(--blue);color:var(--white);font-size:10px}

/* cta */
.cta{position:absolute;top:1850px;width:600px;height:370px;color:var(--white);text-align:center}
.cta.care{left:0;background:linear-gradient(180deg,#2a7fc8,#1667b0)}
.cta.physician{left:600px;background:linear-gradient(180deg,#64bb4c,#4fa53a)}
.cta h2{position:absolute;left:0;width:600px;top:78px;font-family:"Montserrat",Arial,sans-serif;font-weight:600;font-size:19px}
.cta h2::after{content:"";display:block;width:62px;height:2px;background:rgba(255,255,255,.6);margin:12px auto 0}
.cta p{position:absolute;left:150px;width:300px;top:146px;font-size:12px;line-height:20px}
.cta .btn{left:246px;top:244px;width:124px;height:34px;background:var(--white);font-size:12px}
.care .btn{color:var(--blue)}
.physician .btn{color:var(--green);left:202px}
.care .btn{left:246px}

/* reviews */
.review-text{position:absolute;left:404px;width:404px;top:2354px;font-size:12px;line-height:20px;color:#444}
.quote-mark{position:absolute;font-family:Georgia,serif;font-size:78px;color:#ccc;line-height:1}
.round-arrow{position:absolute;top:2424px;width:34px;height:34px;border-radius:50%;border:1px solid #ccc;display:flex;align-items:center;justify-content:center}
.reviewer{position:absolute;left:456px;top:2548px;font-family:"Montserrat",Arial,sans-serif;font-size:10px;font-weight:600;color:#222;line-height:18px}
.reviewer span{display:block;font-family:"PT Sans",Arial,sans-serif;font-weight:400;color:#555}

/* footer */
.footer{position:absolute;left:0;top:2652px;width:1200px;height:343px;background:var(--footer);color:#ddd}
.footer .brand{top:48px;font-size:25px}
.footer h4{position:absolute;font-family:"Montserrat",Arial,sans-serif;font-size:11px;font-weight:700;color:var(--white);letter-spacing:.4px}
.newsletter{position:absolute;left:132px;top:148px;width:262px;height:40px;background:var(--white);display:flex;align-items:center;padding:3px}
.newsletter span{flex:1;padding-left:8px;font-size:11px;color:#555}
.newsletter b{width:76px;height:32px;background:var(--blue);color:var(--white);font-family:"Montserrat",Arial,sans-serif;font-size:10px;display:flex;align-items:center;justify-content:center}
.contact-row{position:absolute;left:500px;display:flex;gap:14px;font-size:11px;line-height:16px;color:#ddd}
.contact-row svg{flex:none;margin-top:2px}
.map{position:absolute;left:810px;top:38px;width:268px;height:210px;background:linear-gradient(135deg,#e9e5dc,#dcd9d0 60%,#cfe0c6)}
.footer-rule{position:absolute;left:130px;top:252px;width:948px;height:1px;background:var(--footer-line)}
.social{position:absolute;top:284px;width:24px;height:24px;border-radius:50%}
.footer-links{position:absolute;left:406px;top:290px;font-size:10px;color:#ddd;text-transform:uppercase}
.copyright{position:absolute;left:880px;top:290px;font-size:10px;color:#ddd}
</style>
</head>
<body>

<header class="hero">
  <div class="abs" role="img" aria-label="Waterfront city skyline at sunset reflected in a river" style="inset:0"></div>
  <div class="brand">Tovren Bay Healthcare</div>
  <nav class="nav">
    <a class="active">Home</a><a>About Us</a><a>Services</a><a>Features</a><a>Testimonials</a><a>Contact Us</a>
  </nav>
  <div class="slide-arrow" style="left:-25px"><svg width="12" height="12" viewBox="0 0 12 12" style="margin-left:24px"><path d="M8 1 3 6l5 5" fill="none" stroke="#333" stroke-width="2"/></svg></div>
  <div class="slide-arrow" style="left:1175px"><svg width="12" height="12" viewBox="0 0 12 12" style="margin-right:24px"><path d="m4 1 5 5-5 5" fill="none" stroke="#333" stroke-width="2"/></svg></div>
  <div class="hero-kicker">PRIMARY CARE</div>
  <div class="hero-title">PHYSICIAN PRACTICE</div>
  <div class="btn">Read More</div>
</header>

<section class="welcome">
  <h2 class="section-title" style="top:690px">WELCOME TO OUR SITE</h2>
  <p class="welcome-text">A physician who provides long-term, comprehensive care in the office and the hospital, managing both common and complex illness of adolescents, adults and the elderly</p>
  <svg class="abs" style="left:320px;top:870px" width="580" height="430" viewBox="0 0 580 430">
    <path d="M6 430 A284 284 0 0 1 574 430" fill="none" stroke="#ddd" stroke-width="2"/>
  </svg>
  <div class="abs" role="img" aria-label="Five smiling women of different ages and backgrounds in pink tops" style="left:340px;top:985px;width:530px;height:313px;background:linear-gradient(180deg,#fff 0%,#f1e6e2 30%,#e9a9c0 75%,#e08fb0 100%)"></div>
  <div class="feature-label" style="left:382px;top:864px">Healthcare</div>
  <div class="feature-label" style="left:540px;top:846px">Treatments</div>
  <div class="feature-label" style="left:706px;top:868px">Support</div>
  <div class="feature-icon" style="left:414px;top:894px"><svg width="26" height="24" viewBox="0 0 26 24"><path d="M13 23 2 12A6.5 6.5 0 0 1 13 3a6.5 6.5 0 0 1 11 9Z" fill="#666"/></svg></div>
  <div class="feature-icon" style="left:566px;top:876px"><svg width="30" height="24" viewBox="0 0 30 24"><path d="M2 4v18M2 16h26v6M6 12h20v4H6z" fill="none" stroke="#666" stroke-width="2.4"/><path d="M14 2v6M11 5h6" stroke="#666" stroke-width="2"/></svg></div>
  <div class="feature-icon" style="left:724px;top:896px"><svg width="26" height="24" viewBox="0 0 26 24"><path d="M4 16v-4a9 9 0 0 1 18 0v4" fill="none" stroke="#666" stroke-width="2.4"/><rect x="2" y="13" width="6" height="9" rx="2" fill="#666"/><rect x="18" y="13" width="6" height="9" rx="2" fill="#666"/></svg></div>
</section>

<section class="treatments">
  <h2 class="section-title" style="top:58px">OUR TREATMENTS</h2>
</section>
<article class="card" style="left:132px">
  <div class="photo" role="img" aria-label="Two young women wearing protective face masks" style="background:linear-gradient(160deg,#c9a27a,#e8e6e4 55%,#3f6f9c)"></div>
  <h3>Disease Prevention</h3>
  <p>There are many variations of passages of Lorem Ipsum availabl.</p>
  <div class="btn">Read More</div>
</article>
<article class="card" style="left:370px">
  <div class="photo" role="img" aria-label="Woman with outstretched arms by a lake at sunrise" style="background:linear-gradient(180deg,#a9c4d8,#e9eef0 45%,#8fa6b4 70%,#5b6f7c)"></div>
  <h3>Wellness</h3>
  <p>There are many variations of passages of Lorem Ipsum availabl.</p>
  <div class="btn">Read More</div>
</article>
<article class="card" style="left:610px">
  <div class="photo" role="img" aria-label="Distressed man sitting at a table with a glass of whisky" style="background:linear-gradient(160deg,#5b4a3e,#8a6a55 50%,#3a2f29)"></div>
  <h3>Substance Abuse</h3>
  <p>There are many variations of passages of Lorem Ipsum availabl.</p>
  <div class="btn">Read More</div>
</article>
<article class="card" style="left:850px">
  <div class="photo" role="img" aria-label="Young woman talking with a counselor" style="background:linear-gradient(160deg,#dfe4e8,#f3f1ee 50%,#c79a78)"></div>
  <h3>Mental Health</h3>
  <p>There are many variations of passages of Lorem Ipsum availabl.</p>
  <div class="btn">Read More</div>
</article>

<section class="cta care" role="img" aria-label="Doctor caring for a patient under a blue overlay">
  <h2>GET CARE NOW</h2>
  <p>Lorem Ipsum is simply dummy text of the printing and typesetting industry. Lorem Ipsum has been the industry's standard dummy text ever</p>
  <div class="btn">Read More</div>
</section>
<section class="cta physician" role="img" aria-label="Physician with stethoscope under a green overlay">
  <h2>PHYSICIAN</h2>
  <p>Lorem Ipsum is simply dummy text of the printing and typesetting industry. Lorem Ipsum has been the industry's standard dummy text ever</p>
  <div class="btn">Read More</div>
</section>

<section class="reviews">
  <h2 class="section-title" style="top:2268px">REVIEWS</h2>
  <div class="quote-mark" style="left:354px;top:2330px">&ldquo;</div>
  <p class="review-text">Lorem ipsum dolor sit amet, consectetur adipiscing elit. Aenean erat velit, tempus nec nisi a, rutrum ultricies ipsum. Donec tincidunt tellus id facilisis eleifend. Aenean dignissim nisl sed aliquam tinciduntMorbi ac fringilla nunc, a sagittis sem. Nulla mattis quis neque et iaculis. Aenean purus lorem, pulvinar et pretium eu, mollis nec quam. Aenean ac arcu metus. Praesent gravida eu eros eu vestibulum. Aenean quis massa non enim pellentesque vehicula. Aenean tincidunt auctor pharetra. Morbi ac orci non massa eleifend congue. Quisque dui eni</p>
  <div class="quote-mark" style="left:628px;top:2496px">&rdquo;</div>
  <div class="round-arrow" style="left:236px"><svg width="8" height="10" viewBox="0 0 8 10"><path d="M6 1 2 5l4 4" fill="none" stroke="#999" stroke-width="1.5"/></svg></div>
  <div class="round-arrow" style="left:888px"><svg width="8" height="10" viewBox="0 0 8 10"><path d="m2 1 4 4-4 4" fill="none" stroke="#999" stroke-width="1.5"/></svg></div>
  <div class="abs" role="img" aria-label="Reviewer portrait" style="left:402px;top:2544px;width:34px;height:34px;border-radius:50%;background:linear-gradient(180deg,#b9a79a,#5d5f66)"></div>
  <div class="reviewer">DANIEL OSTERBY<span>England</span></div>
  <svg class="abs" style="left:726px;top:2564px" width="70" height="12" viewBox="0 0 70 12">
    <g fill="#e8542f">
      <path id="st" d="M6 0l1.8 3.9 4.2.4-3.2 2.8 1 4.1L6 9.1 2.2 11.2l1-4.1L0 4.3l4.2-.4z"/>
      <use href="#st" x="14"/><use href="#st" x="28"/><use href="#st" x="42"/><use href="#st" x="56"/>
    </g>
  </svg>
</section>

<footer class="footer">
  <div class="brand">Tovren Bay Healthcare</div>
  <h4 style="left:132px;top:128px">NEWSLETTER</h4>
  <div class="newsletter"><span>E mail id</span><b>SIGNUP</b></div>

  <h4 style="left:500px;top:54px">CONTACT US</h4>
  <div class="contact-row" style="top:90px"><svg width="9" height="12" viewBox="0 0 9 12"><path d="M4.5 12S0 6.8 0 4.5a4.5 4.5 0 0 1 9 0C9 6.8 4.5 12 4.5 12Z" fill="#ddd"/><circle cx="4.5" cy="4.5" r="1.6" fill="#3b3c3f"/></svg><div>5130 N. HARBORVIEW AVE, SUITE 304<br>LAUDERHILL, FL 33328</div></div>
  <div class="contact-row" style="top:140px"><svg width="10" height="11" viewBox="0 0 10 11"><path d="M2 0h2l1 3-1.5 1a6 6 0 0 0 3 3L7.5 5.5l3 1v2c0 1-1 2-2 2C4 10.5 0 6.5 0 2 0 1 1 0 2 0Z" fill="#ddd"/></svg><div>(954) 555-0136</div></div>
  <div class="contact-row" style="top:174px"><svg width="11" height="9" viewBox="0 0 11 9"><rect width="11" height="9" rx="1" fill="#ddd"/><path d="m0.5 1 5 4 5-4" fill="none" stroke="#3b3c3f" stroke-width="1.2"/></svg><div>info@tovrenbayhealth.example</div></div>

  <div class="map" role="img" aria-label="Street map showing the Lauderhill office location"></div>

  <div class="footer-rule"></div>
  <h4 style="left:130px;top:290px;font-size:10px">FOLLOW US</h4>
  <div class="social" role="img" aria-label="Social profile" style="left:220px;background:#3b5db2"></div>
  <div class="social" role="img" aria-label="Social profile" style="left:254px;background:#27a4e8"></div>
  <div class="social" role="img" aria-label="Social profile" style="left:288px;background:#1c3f82"></div>
  <div class="footer-links">Home | About Us | Services | Features | Testimonials | Contact Us</div>
  <div class="copyright">Copyrights @ 2018 All Rights Reserved</div>
</footer>

</body>
</html>
```